Business Card Design for LeafSpire (Farming Devices)

We need Business Cards for our new Company based in Switzerland called "LeafSpire" We develop innovativ products for indoor and outdoor Farming for household and components for vertical farming. Our initial BloomNook gives people the possibility to grow their own food at home all year round. The design should communicate freshness, innovation, health.

```html
<!DOCTYPE html>
<html lang="en">
<head>
<meta charset="utf-8">
<title>LeafSpire Business Card</title>
<link rel="stylesheet" href="https://fonts.googleapis.com/css2?family=Lato:wght@700&family=Open+Sans:wght@400&display=swap">
<style>
  :root {
    --page-bg: #ececec;
    --card-white: #ffffff;
    --brand-green: #7cb032;
    --card-lime: #b0cc1f;
    --lime-light: #bfd83f;
    --icon-tint: #d6e68f;
    --text-light: #ffffff;
  }
  html, body {
    margin: 0;
    padding: 0;
    width: 1200px;
    height: 914px;
    overflow: hidden;
    background: var(--page-bg);
  }
  .canvas {
    position: relative;
    width: 1200px;
    height: 914px;
  }
  .card {
    position: absolute;
    left: 305px;
    width: 590px;
    height: 336px;
    border-radius: 22px;
    overflow: hidden;
  }
  .card-front {
    top: 101px;
    background: var(--card-white);
    display: flex;
    align-items: center;
    justify-content: center;
  }
  .brand-name {
    margin: 0;
    font-family: "Lato", sans-serif;
    font-weight: 700;
    font-size: 62px;
    letter-spacing: -0.5px;
    color: var(--brand-green);
    transform: translate(-2px, 14px);
  }
  .card-back {
    top: 477px;
    background: var(--card-lime);
  }
  .produce-pattern {
    position: absolute;
    inset: 0;
    background: radial-gradient(ellipse at 50% 50%, var(--card-lime) 35%, var(--lime-light) 100%);
  }
  .contact-list {
    position: absolute;
    left: 185px;
    top: 131px;
    margin: 0;
    padding: 0;
    list-style: none;
    font-family: "Open Sans", sans-serif;
    font-weight: 400;
    color: var(--text-light);
  }
  .contact-item {
    display: flex;
    align-items: center;
    height: 32px;
  }
  .contact-icon {
    width: 16px;
    height: 16px;
    margin-right: 16px;
    flex: none;
  }
  .contact-phone {
    font-size: 20px;
    letter-spacing: 6px;
  }
  .contact-email {
    font-size: 20px;
    letter-spacing: 0.2px;
  }
</style>
</head>
<body>
<main class="canvas">
  <section class="card card-front" aria-label="Card front">
    <h1 class="brand-name">LeafSpire</h1>
  </section>

  <section class="card card-back" aria-label="Card back">
    <div class="produce-pattern" role="img" aria-label="Light line drawings of vegetables, leaves, herbs and fruit scattered across the lime background"></div>
    <ul class="contact-list">
      <li class="contact-item">
        <svg class="contact-icon" viewBox="0 0 16 16" aria-hidden="true">
          <rect width="16" height="16" rx="2" fill="var(--icon-tint)"/>
          <path d="M5 3.5 L6.6 5.4 L5.8 6.6 C6.5 8 7.8 9.4 9.3 10.1 L10.5 9.3 L12.4 10.9 L11.3 12.4 C7.6 12 4 8.3 3.6 4.6 Z" fill="var(--card-lime)"/>
        </svg>
        <span class="contact-phone">+41-22-5550147</span>
      </li>
      <li class="contact-item">
        <svg class="contact-icon" viewBox="0 0 16 16" aria-hidden="true">
          <rect width="16" height="16" rx="2" fill="var(--icon-tint)"/>
          <rect x="3.5" y="5" width="9" height="6.5" fill="none" stroke="var(--card-lime)" stroke-width="1"/>
          <path d="M3.5 5 L8 8.6 L12.5 5" fill="none" stroke="var(--card-lime)" stroke-width="1"/>
        </svg>
        <span class="contact-email">Leafspire@lsproject.com</span>
      </li>
    </ul>
  </section>
</main>
</body>
</html>
```